Carpal Tunnel - PPC Landing Page

We need to do a SINGLE page landing page for a doctor who specializes in Carpal Tunnel syndrome - please research if you're not familiar - it's very common.

Landing page essentials:
Must have a form in upper right hand corner:
Form title: "Get a free diagnosis."
Form inputs: Name, Phone, Email, Requested Appointment time

Page is for PPC, so needs to be simple and light on content. Content has been provided and attached to this project.

No navigation, just a single page.

Industry/Entity Type

Health

Coding

Coded - Design and coding required

Number of Pages Required

1 page

Requirements
Must have
• Elegant look - Conversion optimized for form and phone
• Responsive design.
Should not have
• Old outdated images.

```html
<!DOCTYPE html>
<html lang="en">
<head>
<meta charset="utf-8">
<title>Median Hand Clinic – Get a Free Diagnosis</title>
<link href="https://fonts.googleapis.com/css2?family=Open+Sans:wght@400;600;700&family=Roboto+Condensed:wght@400;700&family=Oswald:wght@400;500;600&display=swap" rel="stylesheet">
<style>
  :root{
    --navy:#0f2d57;
    --navy-deep:#0a2246;
    --blue:#1f6fc2;
    --sky-1:#e4f1fb;
    --sky-2:#b9d9f1;
    --red:#e3262c;
    --teal:#19b3a3;
    --ink:#2f3b4a;
    --text:#5b6470;
    --pale:#eef3f8;
    --white:#ffffff;
    --footer-text:#c9d6e8;
  }
  *{box-sizing:border-box;margin:0;padding:0}
  html,body{width:1200px;height:2324px;overflow:hidden}
  body{font-family:'Open Sans',sans-serif;color:var(--text);background:var(--white);position:relative}

  .topbar{height:36px;background:var(--navy);display:flex;align-items:center;justify-content:space-between;padding:0 40px}
  .site-name{font-family:'Open Sans',sans-serif;font-weight:600;font-size:18px;color:var(--white)}
  .topbar-phone{display:flex;align-items:center;gap:8px;color:var(--white);font-size:15px;font-weight:600}
  .topbar-phone svg{width:16px;height:16px}

  .hero{height:394px;position:relative}
  .hero-photo{position:absolute;inset:0;background:linear-gradient(100deg,var(--sky-1) 0%,#d3e8f7 45%,var(--sky-2) 100%)}

  .lead-form{position:absolute;top:40px;right:100px;width:300px;background:var(--white);box-shadow:0 6px 18px rgba(15,45,87,.18);z-index:2}
  .lead-form h2{background:var(--red);color:var(--white);font-family:'Oswald',sans-serif;font-weight:500;font-size:27px;line-height:1.15;padding:18px 20px;text-transform:uppercase}
  .lead-form .fields{padding:18px 20px 20px;display:flex;flex-direction:column;gap:12px}
  .field{height:36px;border:1px solid #d5dbe2;font-size:12px;color:#99a1ab;display:flex;align-items:center;padding:0 12px}
  .submit{height:40px;background:var(--red);color:var(--white);font-family:'Oswald',sans-serif;font-size:18px;letter-spacing:1px;display:flex;align-items:center;justify-content:center;margin-top:4px}

  .about{height:1180px;padding:100px 32px 0}
  .about h1{font-family:'Roboto Condensed',sans-serif;font-weight:700;font-size:32px;color:var(--ink);text-transform:uppercase;margin-bottom:16px}
  .about p{font-size:13px;line-height:1.85;margin-bottom:12px}
  .about h3{font-family:'Roboto Condensed',sans-serif;font-weight:700;font-size:19px;color:var(--red);text-transform:uppercase;margin:22px 0 12px;border-bottom:1px solid #e4e8ed;padding-bottom:10px}
  .about h4{font-family:'Roboto Condensed',sans-serif;font-weight:700;font-size:14px;color:var(--blue);text-transform:uppercase;margin:18px 0 6px}

  .hours{height:260px;position:relative;color:var(--white);text-align:center}
  .hours-photo{position:absolute;inset:0;background:linear-gradient(180deg,#1b3a66 0%,#10284d 60%,#0c2143 100%)}
  .hours-inner{position:relative;padding-top:40px}
  .hours .label{font-family:'Roboto Condensed',sans-serif;font-size:22px;letter-spacing:1px;text-transform:uppercase}
  .hours .time{font-family:'Oswald',sans-serif;font-weight:500;font-size:54px;text-transform:uppercase;margin:8px 0 24px}
  .hours-cta{display:flex;justify-content:center;align-items:center;gap:28px}
  .btn-red{background:var(--red);color:var(--white);font-family:'Oswald',sans-serif;font-size:16px;letter-spacing:1px;padding:12px 40px;text-transform:uppercase}
  .call{font-family:'Oswald',sans-serif;font-size:20px;text-transform:uppercase;display:flex;gap:10px}
  .call span{color:var(--red)}

  .newsletter{height:344px;background:var(--pale);text-align:center;padding-top:90px}
  .newsletter h2{font-family:'Oswald',sans-serif;font-weight:500;font-size:46px;color:var(--blue);text-transform:uppercase;margin-bottom:36px}
  .subscribe{display:flex;justify-content:center;gap:16px}
  .subscribe .email{width:440px;height:44px;background:var(--white);border:1px solid #d5dbe2;padding:0 16px;font-size:13px;color:#99a1ab;display:flex;align-items:center}
  .subscribe .go{width:200px;height:44px;background:var(--teal);color:var(--white);font-family:'Oswald',sans-serif;font-size:16px;text-transform:uppercase;display:flex;align-items:center;justify-content:center}

  .footer{height:110px;background:var(--navy-deep);display:flex;flex-direction:column;align-items:center;justify-content:center;gap:8px}
  .footer .site-name{color:var(--footer-text)}
  .footer small{font-size:11px;color:#8c9bb0}
</style>
</head>
<body>

<header class="topbar">
  <div class="site-name">Median Hand Clinic</div>
  <div class="topbar-phone">
    <svg viewBox="0 0 24 24" fill="#ffffff"><path d="M6.6 10.8a15.1 15.1 0 0 0 6.6 6.6l2.2-2.2a1 1 0 0 1 1-.25 11.4 11.4 0 0 0 3.6.57 1 1 0 0 1 1 1V20a1 1 0 0 1-1 1A17 17 0 0 1 3 4a1 1 0 0 1 1-1h3.5a1 1 0 0 1 1 1c0 1.25.2 2.45.57 3.57a1 1 0 0 1-.25 1z"/></svg>
    +91 5550 123 456
  </div>
</header>

<section class="hero">
  <div class="hero-photo" role="img" aria-label="Smiling doctor in a white coat with a stethoscope, set against a bright clinic background"></div>
  <form class="lead-form">
    <h2>Get a Free Diagnosis</h2>
    <div class="fields">
      <div class="field">Name</div>
      <div class="field">Phone No</div>
      <div class="field">Email</div>
      <div class="field">Requested Appointment time</div>
      <div class="submit">SUBMIT</div>
    </div>
  </form>
</section>

<main class="about">
  <h1>What is Carpal Tunnel Syndrome</h1>
  <p>In Dr. Halden's clinical practice, Carpal Tunnel Syndrome is one of the most commonly reported health problems. Carpal tunnel occurs when swelling pinches the median nerve, which provides sensation to the palm side of the thumb, index finger, middle finger and to the inside half of the ring finger.</p>
  <p>The result can be a combination of tingling, numbness, weakness and pain in the fingers, thumb, palm or the forearm. If the condition is not treated, permanent deterioration of muscle tissue can occur.</p>

  <h3>Other Conditions Treated by Dr. Halden:</h3>

  <h4>Cubital Tunnel Syndrome (Cell Phone Elbow)</h4>
  <p>Similar to carpal tunnel syndrome, cubital tunnel syndrome is a condition brought on by increased pressure. This occurs when there is increased pressure of the ulnar nerve at the elbow. The bump of bone on the inner portion of the elbow, commonly known as the funny bone, is located under the ulnar nerve. At this sensitive area, the ulnar nerve is located directly next to the bone and over time becomes very susceptible to pressure. As the pressure on the nerve becomes greater, there is a disturbance in how the nerve works, again, similarly to carpal tunnel syndrome, progressive pain, numbness, tingling, and pain is felt in the elbow, forearm, hand and fingers.</p>

  <h4>Dequervains Tenosynovitis</h4>
  <p>Also known as first dorsal compartment tendonitis, this is also one of the most common hand problems seen by Dr. Halden. It is most commonly known as deQuervain's tendinitis or tenosynovitis. Essentially, this is a condition brought on by irritation or inflammation of the tendons found on the thumb side of the wrist. This inflammation causes the sheath around the tendon to swell and enlarge. When this occurs, making thumb and wrist movement painful. For individuals with this condition, making a fist, grasping or holding objects are common painful movements.</p>

  <h4>Dupuytren's Disease</h4>
  <p>Dupuytren's Disease is caused by an abnormal thickening in the palm and fingers. This limits hand movement. Although the actual cause of Dupuytren's is not known, heredity plays a significant role. It commonly affects Caucasians with ancestors from Northern Europe. The condition occurs more frequently in men, runs in families, and usually begins after age 40. Dupuytren's Disease begins as a small lump or pit in the palm, often near the crease at the base of the small or ring finger. As cords form, it can slowly draw the fingers into the palm and affect daily activities.</p>

  <h4>Hand Fractures</h4>
  <p>Fractures of the fingers occur when the finger or hands hit a solid object with force. Fractures are most common at the base of the little finger. This is called a boxer's fracture. Nerve injuries occur as a result of trauma, compression or over-stretching. Nerves send impulses to the brain about sensation and also play an important role in finger movement. When nerves are injured, one can lose ability to move fingers, lose sensation and develop a condition known as a contracture. A nerve injury of the hand can be disabling and results in loss of hand function. Proper care early helps recovery.</p>

  <h4>Hand Sprains</h4>
  <p>Sprains result from forcing a joint to perform a function against its normal range of motion. Finger sprains occur when the ligaments which are attached to the bones are overstretched and this results in pain, swelling, and difficulty for moving the finger. Common examples of a sprain are jammed or twisted fingers. These injuries are common among ball players but can also occur in laborers and family men. When finger sprains are not treated on time, prolonged disability can result.</p>
</main>

<section class="hours">
  <div class="hours-photo" role="img" aria-label="Dim blue-toned photo of a clinic interior behind the opening hours"></div>
  <div class="hours-inner">
    <div class="label">Opening Hours</div>
    <div class="time">Monday to Saturday - 8am to 9pm</div>
    <div class="hours-cta">
      <div class="btn-red">Get Appointment</div>
      <div class="call">Or call us <span>+91 5550 123 456</span></div>
    </div>
  </div>
</section>

<section class="newsletter">
  <h2>Subscribe to our Newsletter</h2>
  <div class="subscribe">
    <div class="email">ENTER YOUR EMAIL</div>
    <div class="go">Subscribe</div>
  </div>
</section>

<footer class="footer">
  <div class="site-name">Median Hand Clinic</div>
  <small>© Copyright 2015. All Rights Reserved by Median Hand Clinic</small>
</footer>

</body>
</html>
```